Präsentationsvorlagen für Automotive Engineering
Zielgruppe
Automotive Engineering - Software & Embedded systems are main focus including V-Modell
Aufgabenstellung
see Logo

```html
<!DOCTYPE html>
<html lang="de">
<head>
<meta charset="utf-8">
<title>NORVANT – Präsentationsvorlage</title>
<link href="https://fonts.googleapis.com/css2?family=Roboto:wght@400;500;700;900&family=Lato:wght@400;700&display=swap" rel="stylesheet">
<style>
:root{
  --navy:#062b5d;
  --navy-deep:#04224b;
  --steel:#0a4f8e;
  --red:#f5233a;
  --red-soft:#ff4d5c;
  --paper:#f0f0f0;
  --white:#ffffff;
  --text-soft:#d5dcea;
}
*{margin:0;padding:0;box-sizing:border-box}
html,body{width:1200px;height:4383px;overflow:hidden;background:var(--white)}
body{position:relative;font-family:"Lato",sans-serif;color:var(--white)}
.slide{position:absolute;left:203px;width:784px;height:442px;overflow:hidden;background:var(--navy)}
.abs{position:absolute}
.tab{position:absolute;left:0;top:23px;width:22px;height:125px;background:var(--red);border-radius:0 14px 14px 0;font:700 20px "Roboto",sans-serif;color:var(--white);padding:6px 0 0 3px}
.side-label{position:absolute;left:8px;top:265px;transform:rotate(-90deg);transform-origin:left top;font-size:10px;color:var(--text-soft);white-space:nowrap;letter-spacing:.2px}
.heading{font-family:"Roboto",sans-serif;font-weight:700}
.body-text{font-size:10.5px;line-height:17px;color:var(--text-soft)}
.photo{position:absolute}
.bullets{list-style:none}
.bullets li{display:flex;align-items:center;gap:20px;font-size:10.5px;color:var(--text-soft);height:32px}
.bullets svg{flex:none}

/* cover */
.cover{top:97px;background:var(--paper)}
.cover .band{left:173px;top:57px;width:611px;height:328px;background:var(--red)}
.cover .band-inner{left:125px;top:92px;width:659px;height:258px;background:var(--red-soft)}
.cover .brand{left:285px;top:168px;font:900 86px "Roboto",sans-serif;letter-spacing:4px;color:var(--white)}

/* toc */
.toc{top:610px}
.toc .title{left:78px;top:52px;font-size:31px}
.toc .item{position:absolute;width:150px}
.toc .item h3{font:500 16px "Roboto",sans-serif;color:var(--red)}
.toc .item p{font-size:10px;line-height:17px;color:var(--text-soft);margin-top:4px;height:40px}
.toc .item .num{font:700 27px "Roboto",sans-serif;color:var(--white);margin-top:6px}

/* foreword */
.foreword{top:1122px}
.quote-bubble{left:288px;top:92px;width:227px;height:245px;background:var(--red);border-radius:50% 50% 48% 48%;text-align:center;padding-top:42px}
.quote-bubble .mark{font:900 38px "Roboto",sans-serif;line-height:30px}
.quote-bubble p{font:700 18px/24px "Roboto",sans-serif;margin-top:12px;padding:0 20px}
.avatar-ring{left:357px;top:300px;width:90px;height:90px;border-radius:50%;border:1.5px dashed var(--red);background:var(--navy)}
.avatar{left:367px;top:310px;width:70px;height:70px;border-radius:50%;background:radial-gradient(circle at 50% 40%,#a87a5e,#3b3f4e)}
.foreword .mini-brand{left:568px;top:142px;font:700 22px "Roboto",sans-serif;letter-spacing:2px}
.foreword .title{left:568px;top:170px;font-size:38px;color:var(--red)}
.foreword .lead{left:570px;top:217px;width:190px;font-size:10px;line-height:17px}
.foreword .name{left:570px;top:278px;font:700 16px "Roboto",sans-serif}
.foreword .role{left:570px;top:298px;font-size:10px;color:var(--text-soft)}

/* intro */
.intro{top:1633px}
.intro .title{left:462px;top:88px;font-size:38px;line-height:47px;color:var(--red)}
.intro .body-text{left:465px;top:215px;width:265px}

/* about */
.about{top:2117px}
.about .title{left:78px;top:45px;font-size:40px;color:var(--red)}
.about .body-text{left:78px;top:95px;width:290px}
.about .bullets{left:78px;top:175px}

/* v-model */
.vmodel{top:2630px}
.vmodel .steel{left:0;top:0;width:135px;height:442px;background:linear-gradient(180deg,var(--steel),#0d5a9e)}
.vmodel .title{left:0;width:784px;top:25px;text-align:center;padding-left:157px;font-size:37px;color:var(--red)}
.vmodel svg.diagram{position:absolute;left:0;top:0}

/* requirements */
.req{top:3142px}
.req .panel{left:142px;top:172px;width:642px;height:270px;background:var(--red)}
.req .title{left:192px;top:233px;font-size:27px}
.req .body-text{left:192px;top:290px;width:490px;color:#ffe3e6;font-size:9.5px;line-height:17.5px}
.req .bullets{top:34px}
.req .bullets li{gap:18px;font-size:10px}

/* contact */
.contact{top:3653px}
.contact .title{left:78px;top:45px;font-size:38px}
.contact .body-text{left:80px;top:95px;width:290px}
.contact-list{position:absolute;left:78px;top:180px;width:302px;list-style:none}
.contact-list li{display:flex;height:70px;align-items:center;border-bottom:1px solid #4a6690}
.contact-list li:last-child{border-bottom:none}
.contact-list .label{width:195px;font:500 16px "Roboto",sans-serif;color:var(--red)}
.contact-list .value{font-size:10px;line-height:16px;color:var(--text-soft)}
.contact .accent{left:600px;top:77px;width:165px;height:170px;background:var(--red)}
.contact .card{left:465px;top:123px;width:268px;height:262px;background:var(--white);display:flex;align-items:center;justify-content:center}
.contact .card span{font:900 44px "Roboto",sans-serif;letter-spacing:3px;color:var(--navy)}
</style>
</head>
<body>

<section class="slide cover">
  <div class="abs band"></div>
  <div class="abs band-inner"></div>
  <div class="abs brand">NORVANT</div>
</section>

<section class="slide toc">
  <div class="tab"></div>
  <div class="side-label">Technologiepräsentation</div>
  <h1 class="abs heading title">INHALTVERZEICHNIS</h1>
  <div class="item" style="left:82px;top:130px"><h3>Über uns</h3><p>Lorem ipsum dolor sit<br>amet dolor</p><div class="num">01</div></div>
  <div class="item" style="left:240px;top:130px"><h3>Lorem ipsum</h3><p>Ipsum lorem dolor sit</p><div class="num">02</div></div>
  <div class="item" style="left:398px;top:130px"><h3>Team</h3><p>Ipsum lorem dolor, sit<br>lorem dolor amet</p><div class="num">03</div></div>
  <div class="item" style="left:82px;top:282px"><h3>Services</h3><p>Lorem ipsum sit amet</p><div class="num">04</div></div>
  <div class="item" style="left:240px;top:282px"><h3>Lorem ipsum</h3><p>Lorem ipsum dolor sit<br>amet dolor</p><div class="num">05</div></div>
  <div class="item" style="left:398px;top:282px"><h3>Kontakt</h3><p>Amet dolor, sit amet dolor<br>lorem ipse</p><div class="num">06</div></div>
  <div class="photo" role="img" aria-label="Nahaufnahme von Zahnrädern eines Getriebes" style="left:550px;top:43px;width:234px;height:354px;background:linear-gradient(135deg,#1f4fb8,#7fa6e6 45%,#c9b98a 65%,#2a55c4)"></div>
</section>

<section class="slide foreword">
  <div class="tab"></div>
  <div class="side-label">Technologiepräsentation</div>
  <div class="abs quote-bubble"><div class="mark">“</div><p>Lorem ipsum dolor sit amet. Dolor lorem amet sit ipse.</p></div>
  <div class="abs avatar-ring"></div>
  <div class="abs avatar" role="img" aria-label="Porträtfoto des Geschäftsführers"></div>
  <div class="abs mini-brand">NORVANT</div>
  <h2 class="abs heading title">Vorwort</h2>
  <p class="abs lead body-text">Lorem ipsum dolor sit amet dolor lorem ipsum sit amet.</p>
  <div class="abs name">Lena Beispiel</div>
  <div class="abs role">Geschäftsführerin</div>
</section>

<section class="slide intro">
  <div class="tab">3</div>
  <div class="side-label">Technologiepräsentation</div>
  <div class="photo" role="img" aria-label="Ingenieure arbeiten im Labor an einer technischen Anlage" style="left:68px;top:45px;width:352px;height:275px;background:linear-gradient(120deg,#1b2c4a,#6d88b4 50%,#c8d4e6 70%,#22355a)"></div>
  <h2 class="abs heading title">Lorem ipsum,<br>dolor sit amet.</h2>
  <p class="abs body-text">Cras maximus fermentum ipsum, id auctor magna maximus a. Lorem ipsum dolor sit amet, consectetur adipiscing elit. Donec dictum enim at diam rhoncus, et facilisis nulla accumsan. Vestibulum maximus id est quis rutrum.</p>
</section>

<section class="slide about">
  <div class="tab">4</div>
  <div class="side-label">Technologiepräsentation</div>
  <h2 class="abs heading title">Über uns</h2>
  <p class="abs body-text">Duis vitae velit dignissim, consequat nisi id, accumsan nunc. Vestibulum nec diam diam. In hac habitasse platea dictumst. Phasellus neque urna, varius sit amet nisi sit amet, vulputate feugiat mauris.</p>
  <ul class="abs bullets">
    <li><svg width="18" height="18" viewBox="0 0 18 18"><circle cx="9" cy="9" r="9" fill="#f5233a"/><path d="M5 9h7M9 6l3 3-3 3" stroke="#fff" stroke-width="1.6" fill="none"/></svg>Praesent id sollicitudin diam</li>
    <li><svg width="18" height="18" viewBox="0 0 18 18"><circle cx="9" cy="9" r="9" fill="#f5233a"/><path d="M5 9h7M9 6l3 3-3 3" stroke="#fff" stroke-width="1.6" fill="none"/></svg>Nulla porta nulla nisl, non aliquet tellus</li>
    <li><svg width="18" height="18" viewBox="0 0 18 18"><circle cx="9" cy="9" r="9" fill="#f5233a"/><path d="M5 9h7M9 6l3 3-3 3" stroke="#fff" stroke-width="1.6" fill="none"/></svg>Donec non finibus dui</li>
    <li><svg width="18" height="18" viewBox="0 0 18 18"><circle cx="9" cy="9" r="9" fill="#f5233a"/><path d="M5 9h7M9 6l3 3-3 3" stroke="#fff" stroke-width="1.6" fill="none"/></svg>Suspendisse sodales sit amet ligula at gravida</li>
  </ul>
  <div class="photo" role="img" aria-label="Softwareentwickler arbeiten an Computern im Büro" style="left:398px;top:0;width:386px;height:442px;clip-path:polygon(115px 0,386px 0,386px 442px,0 442px);background:linear-gradient(150deg,#f2efe9,#d9d6d2 40%,#b53040 70%,#3a3a44)"></div>
</section>

<section class="slide vmodel">
  <div class="tab">6</div>
  <div class="abs steel" role="img" aria-label="Blaue Fläche mit Pixelmuster"></div>
  <h2 class="abs heading title">V-Modell</h2>
  <svg class="diagram" width="784" height="442" viewBox="0 0 784 442" font-family="Lato, sans-serif">
    <defs>
      <marker id="ah" markerWidth="6" markerHeight="6" refX="5" refY="3" orient="auto-start-reverse"><path d="M0 0L6 3L0 6z" fill="#fff"/></marker>
    </defs>
    <rect x="282" y="102" width="93" height="22" fill="none" stroke="#fff" stroke-width="1"/>
    <text x="328" y="117" text-anchor="middle" font-size="9" fill="#fff">Auftragnehmer</text>
    <rect x="563" y="102" width="94" height="22" fill="none" stroke="#fff" stroke-width="1"/>
    <text x="610" y="117" text-anchor="middle" font-size="9" fill="#fff">Auftraggeber</text>
    <text x="472" y="116" text-anchor="middle" font-size="10" font-weight="700" fill="#fff" letter-spacing="1">Validierungs- und</text>
    <text x="472" y="128" text-anchor="middle" font-size="10" font-weight="700" fill="#fff" letter-spacing="1">Testbasis</text>
    <g fill="#fff">
      <polygon points="268,148 385,148 397,198 280,198"/>
      <polygon points="283,215 401,215 413,265 295,265"/>
      <polygon points="300,282 418,282 430,332 312,332"/>
      <polygon points="318,353 435,353 447,400 330,400"/>
      <polygon points="549,148 668,148 656,198 537,198"/>
      <polygon points="530,215 650,215 638,265 518,265"/>
      <polygon points="515,282 630,282 618,332 503,332"/>
      <polygon points="494,353 613,353 601,400 482,400"/>
    </g>
    <g font-size="9" fill="#3b4a6b" text-anchor="middle">
      <text x="333" y="170">Anforderungs-</text><text x="333" y="181">spezifikation</text>
      <text x="348" y="237">Systementwurf-</text><text x="348" y="248">funktional</text>
      <text x="365" y="304">Systementwurf-</text><text x="365" y="315">technisch</text>
      <text x="382" y="374">Modul-</text><text x="382" y="385">spezifikation</text>
      <text x="603" y="177">Abnahmetest</text>
      <text x="584" y="244">Systemtest</text>
      <text x="566" y="311">Integrationstest</text>
      <text x="548" y="380">Modultest</text>
    </g>
    <g stroke="#fff" stroke-width="1.5" marker-start="url(#ah)" marker-end="url(#ah)">
      <line x1="402" y1="173" x2="532" y2="173"/>
      <line x1="418" y1="240" x2="513" y2="240"/>
      <line x1="435" y1="307" x2="498" y2="307"/>
      <line x1="452" y1="377" x2="477" y2="377"/>
    </g>
  </svg>
</section>

<section class="slide req">
  <div class="photo" role="img" aria-label="Hand zeigt auf einen Bildschirm mit Programmcode" style="left:0;top:0;width:222px;height:303px;background:linear-gradient(160deg,#3b4656,#8e98a6 45%,#e6e3de 75%,#c9c3bb)"></div>
  <ul class="abs bullets" style="left:283px">
    <li><svg width="18" height="18" viewBox="0 0 18 18"><circle cx="9" cy="9" r="9" fill="#f5233a"/><path d="M5 9h7M9 6l3 3-3 3" stroke="#fff" stroke-width="1.6" fill="none"/></svg>Nulla porta nulla nisl, non aliquet</li>
    <li><svg width="18" height="18" viewBox="0 0 18 18"><circle cx="9" cy="9" r="9" fill="#f5233a"/><path d="M5 9h7M9 6l3 3-3 3" stroke="#fff" stroke-width="1.6" fill="none"/></svg>Lorem ipsum dolor site amet</li>
    <li><svg width="18" height="18" viewBox="0 0 18 18"><circle cx="9" cy="9" r="9" fill="#f5233a"/><path d="M5 9h7M9 6l3 3-3 3" stroke="#fff" stroke-width="1.6" fill="none"/></svg>Duis vitae velit dignissim</li>
  </ul>
  <ul class="abs bullets" style="left:535px">
    <li><svg width="18" height="18" viewBox="0 0 18 18"><circle cx="9" cy="9" r="9" fill="#f5233a"/><path d="M5 9h7M9 6l3 3-3 3" stroke="#fff" stroke-width="1.6" fill="none"/></svg>Lorem ipsum dolor sit amet</li>
    <li><svg width="18" height="18" viewBox="0 0 18 18"><circle cx="9" cy="9" r="9" fill="#f5233a"/><path d="M5 9h7M9 6l3 3-3 3" stroke="#fff" stroke-width="1.6" fill="none"/></svg>Vestibulum nec diam diam in hac</li>
    <li><svg width="18" height="18" viewBox="0 0 18 18"><circle cx="9" cy="9" r="9" fill="#f5233a"/><path d="M5 9h7M9 6l3 3-3 3" stroke="#fff" stroke-width="1.6" fill="none"/></svg>Varius sit amet nisi sit amet, vulputate</li>
  </ul>
  <div class="abs panel"></div>
  <h2 class="abs heading title">Anforderungsspezifikation</h2>
  <p class="abs body-text">Duis vitae velit dignissim, consequat nisi id, accumsan nunc. Vestibulum nec diam diam. In hac habitasse platea dictumst. Phasellus neque urna, varius sit amet nisi sit amet, vulputate feugiat mauris. Cras molestie convallis condimentum. Vivamus libero eros, blandit nec dui at, iaculis viverra neque. Nam ultricies neque quis dui ultrices sagittis sed ac orci. Praesent id sollicitudin diam. Morbi at ornare lectus. Praesent blandit ante id ex imperdiet congue. Sed eget placerat lorem, semper varius ex.</p>
</section>

<section class="slide contact">
  <div class="tab"></div>
  <h2 class="abs heading title">Kontakt</h2>
  <p class="abs body-text">Duis vitae velit dignissim, consequat nisi id, accumsan nunc. Vestibulum nec diam diam. In hac habitasse platea dictumst. Phasellus neque urna, varius sit amet nisi sit amet, vulputate feugiat mauris. Cras molestie convallis condimentum.</p>
  <ul class="contact-list">
    <li><span class="label">Tel</span><span class="value">+49 123 4567 890</span></li>
    <li><span class="label">E-Mail</span><span class="value">info@norvant.de</span></li>
    <li><span class="label">Adresse</span><span class="value">54321 Beispielstadt,<br>Hauptweg 4</span></li>
    <li><span class="label">Web</span><span class="value">www.norvant.de</span></li>
  </ul>
  <div class="abs accent"></div>
  <div class="abs card"><span>NORVANT</span></div>
</section>

</body>
</html>
```